Bramblewick Painting Epoxy Flyer

We need a promotional flyer for a new epoxy floor coatings division of our painting company. We do epoxy garage floor coatings and paver sealing. It needs to be based on and very similar to the attached flyer. The garage floor picture needs to look more realistic, and the before and after pavers pictures should look less shiny but still a good contrast. Include attached logo

```html
<!DOCTYPE html>
<html lang="en">
<head>
<meta charset="utf-8">
<title>Bramblewick Painting – Epoxy Flyer</title>
<link rel="stylesheet" href="https://fonts.googleapis.com/css2?family=Oswald:wght@500;700&family=Roboto:ital,wght@0,300;0,400;0,500;0,700;0,900;1,300;1,500;1,700&display=swap">
<style>
  :root{
    --green:#3f8a12;
    --green-band:#4a9a1a;
    --blue:#0c3f9a;
    --blue-dark:#0a347f;
    --orange:#d0621a;
    --ink:#1d1d1d;
    --grey-text:#3a3a3a;
    --row-alt:#f3f5f8;
    --stage:#c3c4c6;
    --paper:#ffffff;
  }
  *{margin:0;padding:0;box-sizing:border-box}
  html,body{width:1200px;height:2400px;overflow:hidden;background:var(--stage)}
  body{position:relative;font-family:'Roboto',sans-serif;color:var(--ink)}
  .flyer{position:absolute;left:60px;top:433px;width:1080px;height:1534px;background:var(--paper);overflow:hidden}
  .abs{position:absolute}

  /* brand */
  .brand{left:60px;top:140px;width:380px;display:flex;align-items:center;gap:14px}
  .brand-dot{width:46px;height:46px;border-radius:50%;background:var(--green);flex:none}
  .brand-name{font-family:'Roboto',sans-serif;font-weight:700;font-size:34px;line-height:1.1;color:var(--ink);letter-spacing:.5px}

  /* headline */
  .headline{font-family:'Oswald',sans-serif;font-weight:700;line-height:1;text-transform:uppercase}
  .hl-upgrade{left:500px;top:22px;font-size:134px;color:var(--green);letter-spacing:1px}
  .hl-your{left:503px;top:161px;font-size:86px;color:var(--green)}
  .hl-rule{left:718px;top:199px;width:245px;height:2px;background:linear-gradient(90deg,var(--blue),rgba(12,63,154,0))}
  .hl-garage{left:501px;top:245px;font-size:66px;color:var(--orange);letter-spacing:.5px}

  /* photos */
  .photo{top:359px;height:375px}
  .photo-before{left:19px;width:509px;background:linear-gradient(160deg,#a7a195 0%,#8b8579 45%,#6f695f 100%)}
  .photo-after{left:542px;width:517px;background:linear-gradient(170deg,#c9c9c7 0%,#9a9ea4 40%,#7c828a 100%)}
  .ba-tag{left:350px;top:519px;width:348px;height:56px;background:var(--blue);color:#fff;display:flex;align-items:center;justify-content:center;gap:16px;font-size:35px;font-weight:400;letter-spacing:.5px}
  .ba-tag svg{width:40px;height:20px}

  .subline{left:0;top:772px;width:100%;text-align:center;font-style:italic;font-weight:300;font-size:36px;color:var(--grey-text)}

  /* benefit cards */
  .card{top:833px;width:436px;height:294px;background:#fff;border-radius:14px;box-shadow:0 6px 16px rgba(0,0,0,.10);overflow:hidden}
  .card-left{left:90px}
  .card-right{left:542px}
  .card-head{height:69px;color:#fff;font-size:31px;font-weight:500;padding:20px 0 0 23px;border-radius:14px 14px 0 0;letter-spacing:.3px}
  .card-left .card-head{background:var(--blue)}
  .card-right .card-head{background:var(--green)}
  .card-list{list-style:none}
  .card-list li{height:52px;display:flex;align-items:center;gap:10px;padding-left:18px;font-size:21px;color:var(--grey-text)}
  .card-list li:nth-child(odd){background:var(--row-alt)}
  .card-list svg{width:26px;height:26px;flex:none}

  .tagline{left:0;top:1176px;width:100%;text-align:center;font-family:'Oswald',sans-serif;font-weight:500;font-size:30px;color:var(--ink)}

  /* trust badges */
  .trust{top:1244px;display:flex;align-items:center;gap:10px}
  .trust-icon{width:78px;height:78px;border-radius:50%;background:var(--orange);display:flex;align-items:center;justify-content:center;flex:none}
  .trust-icon svg{width:42px;height:42px}
  .trust-text{font-size:21px;line-height:1.22;color:var(--grey-text)}
  .trust-1{left:108px}
  .trust-2{left:361px}
  .trust-3{left:651px}

  /* footer */
  .footer{left:0;top:1365px;width:1080px;height:169px}
  .footer svg.band{position:absolute;left:0;top:0;width:1080px;height:169px}
  .cta{left:108px;top:1403px;font-weight:700;font-size:35px;line-height:1.25;color:#fff;letter-spacing:.3px}
  .phone{left:462px;top:1372px;display:flex;align-items:center;gap:8px;color:#fff;font-weight:900;font-size:74px;letter-spacing:1px}
  .phone svg{width:46px;height:46px}
  .promise{left:455px;top:1460px;width:550px;height:48px;border:1.5px solid rgba(255,255,255,.75);border-radius:24px;color:#fff;font-style:italic;font-weight:500;font-size:28px;display:flex;align-items:center;justify-content:center}
</style>
</head>
<body>
<main class="flyer">
  <div class="abs brand">
    <span class="brand-dot"></span>
    <span class="brand-name">BRAMBLEWICK PAINTING</span>
  </div>

  <h1 class="abs headline hl-upgrade">Upgrade</h1>
  <div class="abs headline hl-your">Your</div>
  <div class="abs hl-rule"></div>
  <div class="abs headline hl-garage">Garage &amp; Driveway</div>

  <div class="abs photo photo-before" role="img" aria-label="Photo of a worn, stained concrete garage floor before coating"></div>
  <div class="abs photo photo-after" role="img" aria-label="Photo of the same garage with a new grey flake epoxy floor coating"></div>
  <div class="abs ba-tag"><span>BEFORE</span>
    <svg viewBox="0 0 40 20"><path d="M2 10h33M27 3l8 7-8 7" fill="none" stroke="#fff" stroke-width="2.5"/></svg>
    <span>AFTER</span></div>

  <p class="abs subline">From worn-out to like new</p>

  <section class="abs card card-left">
    <h2 class="card-head">EPOXY FLOOR COATINGS</h2>
    <ul class="card-list">
      <li><svg viewBox="0 0 26 26"><circle cx="13" cy="13" r="11" fill="none" stroke="#0c3f9a" stroke-width="2.2"/><path d="M8 13.5l3.5 3.5 7-7.5" fill="none" stroke="#0c3f9a" stroke-width="2.4"/></svg>Durable, long-lasting finish</li>
      <li><svg viewBox="0 0 26 26"><circle cx="13" cy="13" r="11" fill="none" stroke="#0c3f9a" stroke-width="2.2"/><path d="M8 13.5l3.5 3.5 7-7.5" fill="none" stroke="#0c3f9a" stroke-width="2.4"/></svg>Slip-resistant texture</li>
      <li><svg viewBox="0 0 26 26"><circle cx="13" cy="13" r="11" fill="none" stroke="#0c3f9a" stroke-width="2.2"/><path d="M8 13.5l3.5 3.5 7-7.5" fill="none" stroke="#0c3f9a" stroke-width="2.4"/></svg>Covers cracks &amp; imperfections</li>
      <li><svg viewBox="0 0 26 26"><circle cx="13" cy="13" r="11" fill="none" stroke="#0c3f9a" stroke-width="2.2"/><path d="M8 13.5l3.5 3.5 7-7.5" fill="none" stroke="#0c3f9a" stroke-width="2.4"/></svg>Easy to clean &amp; maintain</li>
    </ul>
  </section>

  <section class="abs card card-right">
    <h2 class="card-head">EPOXY FLOOR COATINGS</h2>
    <ul class="card-list">
      <li><svg viewBox="0 0 26 26"><circle cx="13" cy="13" r="11" fill="none" stroke="#3f8a12" stroke-width="2.2"/><path d="M8 13.5l3.5 3.5 7-7.5" fill="none" stroke="#3f8a12" stroke-width="2.4"/></svg>Restores color &amp; enhances appearance</li>
      <li><svg viewBox="0 0 26 26"><circle cx="13" cy="13" r="11" fill="none" stroke="#3f8a12" stroke-width="2.2"/><path d="M8 13.5l3.5 3.5 7-7.5" fill="none" stroke="#3f8a12" stroke-width="2.4"/></svg>Protects from sun fading</li>
      <li><svg viewBox="0 0 26 26"><circle cx="13" cy="13" r="11" fill="none" stroke="#3f8a12" stroke-width="2.2"/><path d="M8 13.5l3.5 3.5 7-7.5" fill="none" stroke="#3f8a12" stroke-width="2.4"/></svg>Helps prevent weeds &amp; sand loss</li>
      <li><svg viewBox="0 0 26 26"><circle cx="13" cy="13" r="11" fill="none" stroke="#3f8a12" stroke-width="2.2"/><path d="M8 13.5l3.5 3.5 7-7.5" fill="none" stroke="#3f8a12" stroke-width="2.4"/></svg>Easier to clean &amp; maintain</li>
    </ul>
  </section>

  <p class="abs tagline">Practical upgrades that protect and improve your home</p>

  <div class="abs trust trust-1">
    <span class="trust-icon"><svg viewBox="0 0 42 42"><rect x="9" y="6" width="24" height="30" rx="2" fill="none" stroke="#fff" stroke-width="2.5"/><path d="M14 14h14M14 20h14M14 26h8" stroke="#fff" stroke-width="2.5"/></svg></span>
    <span class="trust-text">Licensed<br>&amp; Insured</span>
  </div>
  <div class="abs trust trust-2">
    <span class="trust-icon"><svg viewBox="0 0 42 42"><path d="M6 21L21 8l15 13M11 18v16h20V18" fill="none" stroke="#fff" stroke-width="2.5"/><rect x="18" y="25" width="6" height="9" fill="#fff"/></svg></span>
    <span class="trust-text">Family-Owned<br>Local Business</span>
  </div>
  <div class="abs trust trust-3">
    <span class="trust-icon"><svg viewBox="0 0 42 42"><path d="M21 37s-11-11-11-20a11 11 0 0 1 22 0c0 9-11 20-11 20z" fill="none" stroke="#fff" stroke-width="2.5"/><circle cx="21" cy="17" r="4" fill="#fff"/></svg></span>
    <span class="trust-text">Serving Fernhollow<br>&amp; Surrounding Areas</span>
  </div>

  <div class="abs footer">
    <svg class="band" viewBox="0 0 1080 169" preserveAspectRatio="none">
      <rect width="1080" height="169" fill="#0c3f9a"/>
      <polygon points="0,0 430,0 392,169 0,169" fill="#4a9a1a"/>
    </svg>
  </div>
  <p class="abs cta">CALL FOR A<br>FREE ESTIMATE</p>
  <div class="abs phone">
    <svg viewBox="0 0 24 24"><path fill="#fff" d="M6.6 10.8a15.1 15.1 0 0 0 6.6 6.6l2.2-2.2a1 1 0 0 1 1-.25 11.4 11.4 0 0 0 3.6.57 1 1 0 0 1 1 1V20a1 1 0 0 1-1 1A17 17 0 0 1 3 4a1 1 0 0 1 1-1h3.5a1 1 0 0 1 1 1c0 1.25.2 2.45.57 3.57a1 1 0 0 1-.25 1z"/></svg>
    <span>555-014-2374</span>
  </div>
  <p class="abs promise">Fast, professional service you can trust</p>
</main>
</body>
</html>
```